Brightwell Cleaning Services - Redesign

I've got my website designed a few years ago and it looks dated now. I would like to get a modern, happy, bright, and clean look. All the content needed can be found at my current website www.brightwellhq.example. Not necessarily need to use all of it, since I want something more clean and easy to read.
I need a 5 pages website:
HOME | SERVICES | ESTIMATE |TESTIMONIALS | CONTACT US

Industry/Entity Type

Janitorial Service

Number of Pages Required

5+ page

Colors
0792cd
34a6d7
85cae6
cee9f5
ebebeb
f0f0f0
f5f5f5
b1b1b1
000000

Requirements
Must have
• Who we are?
• Brightwell Cleaning Services is a local, family-owned, client-focused house and office cleaning company that strives to ensure the highest level of customer satisfaction. We offer expert residential and commercial cleaning services to all the Seattle and Eastside areas.
• Why Brightwell?
• √ We are insured, bonded and licensed.
•  Brightwell Cleaning Service is Fully Insured so you can rest easy knowing your home is protected.
•  Copy of insurance available upon request.
•

√ We provide all supplies and equipments needed to thoroughly clean your home or business.

• √ We are not a franchise. We are a local, family-owned company.

• When you call Brightwell Cleaning Services, you’ll always speak to one of the owners, which is a great benefit to you since this allows us to give you the personal attention and more time needed to clean your home the way you want it cleaned.

• √ We are good at what we do, and we like doing it.

```html
<!DOCTYPE html>
<html lang="en">
<head>
<meta charset="utf-8">
<title>Brightwell Cleaning Services</title>
<link href="https://fonts.googleapis.com/css2?family=Raleway:wght@400;500;600;700&family=Open+Sans:ital,wght@0,400;0,600;0,700;1,400&display=swap" rel="stylesheet">
<style>
:root{
  --blue:#0792cd;
  --blue-mid:#34a6d7;
  --blue-light:#85cae6;
  --blue-pale:#cee9f5;
  --grey-1:#ebebeb;
  --grey-2:#f0f0f0;
  --grey-3:#f5f5f5;
  --grey-4:#b1b1b1;
  --ink:#000;
  --text:#555;
  --gold:#f0b82e;
  --white:#fff;
}
*{box-sizing:border-box;margin:0;padding:0}
html,body{width:1200px;height:2442px;overflow:hidden}
body{font-family:"Open Sans",Arial,sans-serif;color:var(--text);background:var(--white);position:relative}
a{color:inherit;text-decoration:none}
.heading{font-family:"Raleway",Arial,sans-serif;font-weight:700;color:var(--ink);text-transform:uppercase;font-size:22px;letter-spacing:.3px;white-space:nowrap}
.heading span{color:var(--blue-mid)}
.read-more{font-family:"Open Sans",Arial,sans-serif;font-weight:700;font-size:12px;color:var(--blue)}

/* header */
.site-header{position:absolute;top:0;left:0;width:1200px;height:98px;border-top:5px solid var(--blue-mid);background:var(--white)}
.brand{position:absolute;left:95px;top:28px;display:flex;align-items:center;gap:10px}
.brand-mark{width:22px;height:22px;background:var(--blue)}
.brand-name{font-family:"Raleway",Arial,sans-serif;font-weight:700;font-size:36px;color:var(--blue)}
.top-contact{position:absolute;right:98px;top:13px;display:flex;align-items:center;gap:12px;font-size:14px;color:#333}
.top-contact .ic{width:26px;height:26px}
.top-contact .phone{font-size:20px;font-weight:600;color:var(--blue)}
.main-nav{position:absolute;right:98px;top:63px;display:flex;gap:46px;font-family:"Raleway",Arial,sans-serif;font-weight:600;font-size:15px;color:#111}
.main-nav .active{color:var(--blue-mid);position:relative}
.main-nav .active::after{content:"";position:absolute;left:50%;top:25px;width:12px;height:12px;border-left:2px solid var(--blue-mid);border-top:2px solid var(--blue-mid);transform:translateX(-50%) rotate(45deg)}

/* hero */
.hero{position:absolute;top:98px;left:0;width:1200px;height:426px;background:linear-gradient(120deg,#8c8fb0 0%,#cfd5e4 35%,#eef2f7 50%,#c9cfe0 70%,#7f86a8 100%)}
.hero-panel{position:absolute;left:316px;top:91px;width:568px;height:247px;background:rgba(255,255,255,.78);text-align:center;padding-top:24px}
.hero-panel h1{font-family:"Raleway",Arial,sans-serif;font-weight:700;font-size:29px;color:#111;white-space:nowrap;letter-spacing:-.2px}
.hero-panel p{font-size:16px;line-height:26px;color:#222;margin:12px 40px 0}
.btn{display:inline-block;background:var(--blue-mid);color:var(--white);font-family:"Raleway",Arial,sans-serif;font-weight:700;font-size:15px;padding:14px 22px;margin-top:20px}
.dots{position:absolute;left:540px;top:378px;display:flex;gap:4px}
.dots i{width:27px;height:6px;background:var(--grey-4)}
.dots i:first-child{background:var(--blue-mid)}

/* find location */
.locator{position:absolute;top:524px;left:0;width:1200px;height:78px;background:var(--blue-mid)}
.locator-label{position:absolute;left:98px;top:20px;display:flex;align-items:center;gap:14px;color:var(--white);font-family:"Raleway",Arial,sans-serif;font-weight:600;font-size:22px}
.zip{position:absolute;left:380px;top:17px;width:584px;height:44px;background:var(--white);font-size:12px;color:#333;padding:14px 20px}
.zip-btn{position:absolute;left:964px;top:17px;width:138px;height:44px;background:var(--grey-1);font-family:"Raleway",Arial,sans-serif;font-weight:700;font-size:15px;color:#333;text-align:center;line-height:44px}

/* welcome */
.welcome{position:absolute;top:602px;left:0;width:1200px;height:246px}
.welcome .heading{position:absolute;left:98px;top:52px}
.welcome p{position:absolute;left:98px;top:100px;width:720px;font-size:12px;line-height:25px}
.welcome .read-more{position:absolute;left:100px;top:196px}
.badge{position:absolute;left:842px;top:22px;width:200px;height:200px;border-radius:50%;background:var(--gold)}

/* services */
.services{position:absolute;top:848px;left:0;width:1200px;height:462px;background:var(--grey-3)}
.services .heading{position:absolute;left:0;width:1200px;text-align:center;top:46px}
.service{position:absolute;top:104px;width:241px}
.service .photo{height:160px;border:3px solid var(--white);border-radius:6px;box-shadow:0 0 0 1px #ddd}
.service h3{font-family:"Raleway",Arial,sans-serif;font-weight:600;font-size:18px;color:#222;margin-top:20px;white-space:nowrap}
.service p{font-size:12px;line-height:23px;margin-top:8px;height:70px}
.service .read-more{display:block;margin-top:10px}

/* three columns */
.info{position:absolute;top:1310px;left:0;width:1200px;height:443px}
.col{position:absolute;top:42px}
.col .heading{font-size:21px}
.why{left:98px;width:320px}
.why ul{list-style:none;margin-top:30px}
.why li{position:relative;padding-left:30px;font-size:12px;line-height:21px;margin-bottom:16px}
.why li svg{position:absolute;left:0;top:3px;width:14px;height:14px}
.who{left:448px;width:300px}
.video{margin-top:30px;height:148px;border:4px solid var(--white);box-shadow:0 0 0 1px #ccc;background:linear-gradient(90deg,#8a5a2e 0%,#c9b8a4 40%,#e6edf3 70%,#aac6de 100%);position:relative}
.video .play{position:absolute;left:50%;top:50%;width:48px;height:48px;margin:-24px 0 0 -24px}
.who p{font-size:12px;line-height:23px;margin-top:10px}
.news{left:786px;width:320px}
.news-item{display:flex;gap:16px;margin-top:22px}
.news-item:first-of-type{margin-top:30px}
.thumb{width:80px;height:75px;flex:none;border:3px solid var(--white);box-shadow:0 0 0 1px #ccc}
.news-item h4{font-family:"Open Sans",Arial,sans-serif;font-weight:600;font-size:13px;line-height:22px;color:#222;text-transform:uppercase}
.meta{font-size:12px;color:var(--blue);margin-top:6px}
.col .read-more{display:block;margin-top:12px}

/* testimonial */
.testimonial{position:absolute;top:1753px;left:0;width:1200px;height:184px;background:var(--blue-mid);color:var(--white)}
.quote-disc{position:absolute;left:105px;top:42px;width:110px;height:110px;border-radius:50%;background:var(--grey-1)}
.portrait{position:absolute;left:175px;top:38px;width:114px;height:114px;border-radius:50%;background:linear-gradient(160deg,#e3e3e3,#8a8f96);border:3px solid var(--white)}
.testimonial blockquote{position:absolute;left:320px;top:42px;width:790px;font-style:italic;font-size:13px;line-height:25px}
.testimonial cite{position:absolute;left:320px;top:126px;font-style:normal;font-family:"Raleway",Arial,sans-serif;font-weight:500;font-size:16px;letter-spacing:1px}
.arrow{position:absolute;top:78px;width:14px;height:24px}

/* contact */
.contact{position:absolute;top:1937px;left:0;width:1200px;height:428px;background:linear-gradient(180deg,#3a4754,#2a3540)}
.contact .heading{position:absolute;left:0;width:1200px;text-align:center;top:48px;color:var(--white)}
.sub{position:absolute;font-family:"Open Sans",Arial,sans-serif;font-weight:600;font-size:15px;color:var(--white);text-transform:uppercase}
.label{position:absolute;font-size:11px;color:var(--white);text-transform:uppercase}
.field{position:absolute;background:var(--white)}
.submit{position:absolute;left:642px;top:347px;border:2px solid var(--white);color:var(--white);font-weight:700;font-size:13px;padding:8px 14px}
.detail{position:absolute;left:809px;display:flex;align-items:center;gap:18px;font-size:12px;line-height:22px;color:var(--white)}
.detail svg{width:38px;height:38px;flex:none}
.social{position:absolute;left:809px;top:366px;display:flex;gap:14px}
.social i{width:26px;height:26px;background:var(--white);border-radius:3px}

/* footer */
.site-footer{position:absolute;top:2365px;left:0;width:1200px;height:77px;background:var(--white)}
.site-footer p{position:absolute;left:98px;top:30px;font-size:12px;color:#444}
.cards{position:absolute;right:98px;top:22px;display:flex;gap:6px}
.cards span{width:56px;height:34px;border-radius:3px;background:var(--grey-2);border:1px solid var(--grey-4);font-size:10px;font-weight:700;color:#333;text-align:center;line-height:32px}
</style>
</head>
<body>

<svg width="0" height="0" style="position:absolute">
  <defs>
    <symbol id="tick" viewBox="0 0 14 14"><circle cx="7" cy="7" r="7" fill="#0792cd"/><path d="M3.5 7.2 L6 9.6 L10.5 4.6" fill="none" stroke="#fff" stroke-width="1.8"/></symbol>
  </defs>
</svg>

<header class="site-header">
  <a class="brand" href="#"><span class="brand-mark"></span><span class="brand-name">Brightwell</span></a>
  <div class="top-contact">
    <svg class="ic" viewBox="0 0 26 26"><circle cx="13" cy="13" r="12" fill="none" stroke="#0792cd" stroke-width="1.5"/><rect x="7" y="9" width="12" height="8" fill="#0792cd"/><path d="M7 9 L13 14 L19 9" fill="none" stroke="#fff" stroke-width="1"/></svg>
    <span>info@brightwellhq.example</span>
    <svg class="ic" viewBox="0 0 26 26"><circle cx="13" cy="13" r="12" fill="none" stroke="#0792cd" stroke-width="1.5"/><path d="M9 7 L11 7 L12 10 L10.5 11.5 Q12 14.5 14.5 15.5 L16 14 L19 15 L19 17 Q18 19 16 19 Q8 17 7 9 Q7 7 9 7Z" fill="#0792cd"/></svg>
    <span>Call Now :</span><span class="phone">425-555-0148</span>
  </div>
  <nav class="main-nav">
    <a class="active" href="#">HOME</a><a href="#">SERVICES</a><a href="#">ESTIMATE</a><a href="#">TESTIMONIALS</a><a href="#">CONTACT US</a>
    <svg width="14" height="14" viewBox="0 0 14 14" style="margin-top:2px"><circle cx="6" cy="6" r="4.5" fill="none" stroke="#111" stroke-width="2"/><path d="M9.5 9.5 L13 13" stroke="#111" stroke-width="2"/></svg>
  </nav>
</header>

<section class="hero" role="img" aria-label="Bright, clean office lobby with reception desk, potted plants and blue armchairs">
  <div class="hero-panel">
    <h1>BRIGHTWELL CLEANING SERVICES</h1>
    <p>Brightwell Cleaning Services is a locally owned, client-focused house and office cleaning company that strives to ensure the highest level of customer satisfaction.</p>
    <a class="btn" href="#">REQUEST AN ESTIMATE</a>
  </div>
  <div class="dots"><i></i><i></i><i></i><i></i></div>
</section>

<section class="locator">
  <div class="locator-label">
    <svg width="30" height="40" viewBox="0 0 30 40"><path d="M15 1 C7 1 2 7 2 14 C2 24 15 39 15 39 C15 39 28 24 28 14 C28 7 23 1 15 1Z" fill="#fff"/><circle cx="15" cy="14" r="5" fill="#34a6d7"/></svg>
    FIND A LOCATION
  </div>
  <div class="zip">ENTER ZIP CODE</div>
  <div class="zip-btn">SEARCH</div>
</section>

<section class="welcome">
  <h2 class="heading">Welcome to <span>Brightwell Cleaning Services</span></h2>
  <p>Brightwell Cleaning Services is a locally owned, client-focused house and office cleaning company that strives to ensure the highest level of customer satisfaction. We offer expert residential and commercial cleaning services to the Seattle, Redmond, Kirkland, Bothell, Sammamish, Issaquah, Woodinville, Medina, Mercer Island, Renton, and surrounding areas.</p>
  <a class="read-more" href="#">READ MORE &gt;&gt;</a>
  <div class="badge" role="img" aria-label="Satisfaction guarantee seal"></div>
</section>

<section class="services">
  <h2 class="heading">Our <span>Services</span></h2>
  <article class="service" style="left:98px">
    <div class="photo" role="img" aria-label="Modern office with meeting table" style="background:linear-gradient(135deg,#e9ecef,#9ea3a8)"></div>
    <h3>Office Cleaning</h3>
    <p>We clean large or small office buildings, medical clinics/facilities, banks, department and retail stores..</p>
    <a class="read-more" href="#">READ MORE &gt;&gt;</a>
  </article>
  <article class="service" style="left:352px">
    <div class="photo" role="img" aria-label="Cosy living room with sofas and fireplace" style="background:linear-gradient(135deg,#c9a37a,#6b4a2e)"></div>
    <h3>Residential Cleaning</h3>
    <p>Brightwell Cleaning Services offer top quality homes and apartments cleaning services within Seattle, Redmond,..</p>
    <a class="read-more" href="#">READ MORE &gt;&gt;</a>
  </article>
  <article class="service" style="left:606px">
    <div class="photo" role="img" aria-label="Empty room with wood floor and fireplace" style="background:linear-gradient(135deg,#f0dca6,#9a6a3c)"></div>
    <h3>Move Out/In Cleaning</h3>
    <p>Are planning on selling your property, Or your tenancy agreement come to an end? Then this service is especially ..</p>
    <a class="read-more" href="#">READ MORE &gt;&gt;</a>
  </article>
  <article class="service" style="left:860px">
    <div class="photo" role="img" aria-label="Classroom with rows of desks" style="background:linear-gradient(135deg,#d8e4e6,#b69a76)"></div>
    <h3>School/Daycare Cleaning</h3>
    <p>BCS is capable of tracking recess project work in a timely fashion. From floor waxing to classroom painting,..</p>
    <a class="read-more" href="#">READ MORE &gt;&gt;</a>
  </article>
</section>

<section class="info">
  <div class="col why">
    <h2 class="heading">Why <span>Brightwell?</span></h2>
    <ul>
      <li><svg><use href="#tick"/></svg>We are insured, bonded and licensed.</li>
      <li><svg><use href="#tick"/></svg>Brightwell Cleaning Service is Fully Insured so you can rest easy knowing your home is protected.</li>
      <li><svg><use href="#tick"/></svg>Copy of insurance available upon request.</li>
      <li><svg><use href="#tick"/></svg>We provide all supplies and equipments needed to thoroughly clean your home orbusiness.</li>
      <li><svg><use href="#tick"/></svg>We are not a franchise. We are a local, family owned company.</li>
      <li><svg><use href="#tick"/></svg>We are good at what we do, and we like doing it.</li>
    </ul>
    <a class="read-more" href="#">READ MORE &gt;&gt;</a>
  </div>
  <div class="col who">
    <h2 class="heading">Who <span>we are?</span></h2>
    <div class="video" role="img" aria-label="Video still of cleaners wiping a glass door">
      <svg class="play" viewBox="0 0 48 48"><circle cx="24" cy="24" r="23" fill="#222" fill-opacity=".85"/><path d="M19 14 L34 24 L19 34Z" fill="#fff"/></svg>
    </div>
    <p>Brightwell Cleaning Services is a local, familyowned, client-focused house and office cleaning company that strives to ensure the highest level of customer satisfaction. We offer expert residential and commercial ...</p>
    <a class="read-more" href="#">READ MORE &gt;&gt;</a>
  </div>
  <div class="col news">
    <h2 class="heading">Latest <span>News</span></h2>
    <div class="news-item">
      <div class="thumb" role="img" aria-label="Clean hallway" style="background:linear-gradient(135deg,#f2f4f6,#a9b4bf)"></div>
      <div><h4>Nemo enim ipsam voluptatemq uia voluptas sit asper</h4><div class="meta">&#9638; 04/04/2016 &nbsp;|&nbsp; &#9679; Sam Rivera</div></div>
    </div>
    <div class="news-item">
      <div class="thumb" role="img" aria-label="Window washers on a glass facade" style="background:linear-gradient(135deg,#3c6fb0,#9bb8d9)"></div>
      <div><h4>Nemo enim ipsam voluptatemq uia voluptas sit asper</h4><div class="meta">&#9638; 04/04/2016 &nbsp;|&nbsp; &#9679; Sam Rivera</div></div>
    </div>
    <div class="news-item">
      <div class="thumb" role="img" aria-label="Cleaning team with supplies" style="background:linear-gradient(135deg,#f4f4f4,#4d8cc8)"></div>
      <div><h4>Nemo enim ipsam voluptatemq uia voluptas sit asper</h4><div class="meta">&#9638; 04/04/2016 &nbsp;|&nbsp; &#9679; Sam Rivera</div></div>
    </div>
    <a class="read-more" href="#">VIEW MORE &gt;&gt;</a>
  </div>
</section>

<section class="testimonial">
  <svg class="arrow" style="left:76px" viewBox="0 0 14 24"><path d="M12 2 L3 12 L12 22" fill="none" stroke="#fff" stroke-width="2.5"/></svg>
  <div class="quote-disc"></div>
  <div class="portrait" role="img" aria-label="Portrait of the client giving the testimonial"></div>
  <blockquote>It is a long established fact that a reader will be distracted by the readable content of a page when looking at its layout. The point of using Lorem Ipsum is that it has a more-or-less normal distribution of letters, as opposed to using 'Content here, content here', making it look like readable English.</blockquote>
  <cite>Marcus Hale</cite>
  <svg class="arrow" style="left:1112px" viewBox="0 0 14 24"><path d="M2 2 L11 12 L2 22" fill="none" stroke="#fff" stroke-width="2.5"/></svg>
</section>

<section class="contact">
  <h2 class="heading">Contact <span>Us</span></h2>

  <div class="sub" style="left:98px;top:78px">Contact Form</div>
  <div class="label" style="left:98px;top:114px">Name :</div>
  <div class="field" style="left:98px;top:132px;width:313px;height:34px"></div>
  <div class="label" style="left:419px;top:114px">Phone :</div>
  <div class="field" style="left:419px;top:132px;width:311px;height:34px"></div>
  <div class="label" style="left:98px;top:177px">Email :</div>
  <div class="field" style="left:98px;top:195px;width:632px;height:33px"></div>
  <div class="label" style="left:98px;top:236px">Message :</div>
  <div class="field" style="left:98px;top:254px;width:632px;height:82px"></div>
  <div class="submit">SUBMIT</div>

  <div class="sub" style="left:809px;top:78px">Contact Information</div>
  <div class="detail" style="top:126px"><svg viewBox="0 0 38 38"><circle cx="19" cy="19" r="18" fill="none" stroke="#fff" stroke-width="1.5"/><path d="M19 9 C14.5 9 12 12.5 12 16 C12 21.5 19 29 19 29 C19 29 26 21.5 26 16 C26 12.5 23.5 9 19 9Z" fill="#fff"/><circle cx="19" cy="16" r="2.8" fill="#2f3b48"/></svg><span>Street # 200 - 315<br>Lakeview Oregon 97630</span></div>
  <div class="detail" style="top:193px"><svg viewBox="0 0 38 38"><circle cx="19" cy="19" r="18" fill="#fff"/><rect x="10" y="13" width="18" height="12" fill="#2f3b48"/><path d="M10 13 L19 20 L28 13" fill="none" stroke="#fff" stroke-width="1.3"/></svg><span>info@brightwellhq.example</span></div>
  <div class="detail" style="top:250px"><svg viewBox="0 0 38 38"><circle cx="19" cy="19" r="18" fill="none" stroke="#fff" stroke-width="1.5"/><path d="M13 11 L16 11 L17.5 15 L15.5 17 Q17.5 21 21 22.5 L23 20.5 L27 22 L27 25 Q25.5 27 23 27 Q12 25 11 13 Q11 11 13 11Z" fill="#fff"/></svg><span>425-555-0148</span></div>
  <div class="sub" style="left:809px;top:318px">Social</div>
  <div class="social"><i></i><i></i><i></i><i></i><i></i></div>
</section>

<footer class="site-footer">
  <p>Copyright © 2016, Brightwell. All Rights Reserved.</p>
  <div class="cards"><span>Northpay</span><span>Crestcard</span><span>Finlo</span><span>Ledgerly</span></div>
</footer>

</body>
</html>
```